One-Page Promo flyer for Keynote Speaker Profile

Our CEO speaks at professional conferences and business events. We need to create a one-pager to promote his profile to events companies so they may select him to speak at their professional and industry events. He is a paid speaker so this flyer will be used as a selling tool. Please see the brief document for more details. Key aspects that need to be highlighted: company name, left panel as per the brief document.
Target Market(s)
corporate, business, professionals
Industry/Entity Type
Events

```html
<!DOCTYPE html>
<html lang="en">
<head>
<meta charset="utf-8">
<title>Daniel Mercer Stone – Speaker Profile</title>
<link rel="stylesheet" href="https://fonts.googleapis.com/css2?family=Cinzel:wght@600;700&family=Lato:wght@400;700;900&family=Arimo:wght@400&display=swap">
<style>
  :root {
    --blue: #0a4ea3;
    --gold: #fdc211;
    --gold-text: #c99a0e;
    --ink: #1f1f1f;
    --body: #3a3a3a;
    --white: #ffffff;
    --paper: #f7f7f7;
  }
  * { margin: 0; padding: 0; box-sizing: border-box; }
  html, body { width: 933px; height: 1200px; overflow: hidden; background: var(--white); }
  .flyer { position: relative; width: 933px; height: 1200px; overflow: hidden;
    background: radial-gradient(ellipse at 50% 75%, #ffffff 0%, var(--paper) 70%); }

  .masthead { position: absolute; left: 0; top: 0; width: 933px; height: 150px; background: var(--blue); }
  .masthead svg { position: absolute; inset: 0; }
  .speaker-name { position: absolute; left: 93px; width: 765px; top: 26px; text-align: center;
    font-family: 'Cinzel', serif; font-weight: 700; font-size: 48px; color: var(--blue); letter-spacing: 1px; line-height: 1; }
  .speaker-role { position: absolute; left: 93px; width: 765px; top: 92px; text-align: center;
    font-family: 'Lato', sans-serif; font-weight: 700; font-size: 24px; color: var(--ink); letter-spacing: 4.5px; }

  .intro { position: absolute; left: 0; top: 158px; width: 933px; height: 348px; }
  .photo-stage { position: absolute; inset: 0;
    background: linear-gradient(100deg, #d9c7ae 0%, #b49a80 30%, #5b4a42 55%, #e4d8c8 80%); }
  .intro svg { position: absolute; inset: 0; }
  .bio { position: absolute; right: 28px; top: 50px; width: 422px;
    font-family: 'Lato', sans-serif; font-weight: 700; font-size: 22px; line-height: 29.5px; color: var(--white);
    text-align: justify; text-align-last: right; hyphens: auto; -webkit-hyphens: auto; }

  .praise { position: absolute; left: 0; top: 516px; width: 933px; height: 134px; background: var(--gold); }
  .praise::after { content: ""; position: absolute; left: 0; right: 0; top: 134px; height: 16px;
    background: radial-gradient(ellipse at 50% 0%, rgba(0,0,0,0.28), rgba(0,0,0,0) 70%); }
  .praise-text { position: absolute; left: 50px; right: 28px; top: 20px;
    font-family: 'Lato', sans-serif; font-weight: 900; font-size: 22px; line-height: 30px; color: var(--white);
    text-transform: uppercase; text-align: justify; letter-spacing: 0.3px; }
  .quote-mark { font-family: Georgia, serif; font-size: 34px; line-height: 0; position: relative; top: 6px; }
  .quote-open { position: absolute; left: 22px; top: 36px; font-family: Georgia, serif; font-weight: 700; font-size: 42px; color: var(--white); line-height: 0; }

  .highlight { position: absolute; left: 36px; top: 680px; width: 820px;
    font-family: 'Lato', sans-serif; font-size: 21.5px; line-height: 29px; color: var(--body); }

  .topics-title { position: absolute; left: 36px; top: 800px;
    font-family: 'Cinzel', serif; font-weight: 700; font-size: 37px; color: var(--gold-text); letter-spacing: 1px; }
  .topics { position: absolute; left: 38px; top: 872px; width: 500px; list-style: none; }
  .topic { position: relative; padding-left: 26px; }
  .topic h3 { font-family: 'Arimo', sans-serif; font-weight: 400; font-size: 20px; color: var(--blue); line-height: 24px; }
  .topic h3::before { content: ""; position: absolute; left: 2px; top: 7px; width: 10px; height: 10px; border-radius: 50%; background: var(--blue); }
  .topic p { margin: 9px 0 0 2px; font-family: 'Lato', sans-serif; font-size: 15.5px; line-height: 20px; color: var(--body); text-align: justify; }
  .topic + .topic { margin-top: 13px; }

  .portrait { position: absolute; left: 555px; top: 822px; width: 378px; height: 322px;
    background: radial-gradient(ellipse at 55% 55%, #f2ede6 0%, #e8e2d8 45%, rgba(247,247,247,0) 75%); }

  .footer-rule { position: absolute; left: 0; top: 1143px; width: 933px; height: 6px; background: var(--gold); }
  .footer { position: absolute; left: 0; top: 1149px; width: 933px; height: 51px; background: var(--blue); }
</style>
</head>
<body>
<div class="flyer">

  <header class="masthead">
    <svg width="933" height="150" viewBox="0 0 933 150">
      <polygon points="135,8 811,8 858,79 811,150 135,150 93,79" fill="var(--gold)" stroke="var(--white)" stroke-width="5"/>
    </svg>
    <h1 class="speaker-name">Daniel Mercer Stone</h1>
    <p class="speaker-role">MARKETING AND SALES STRATEGIST</p>
  </header>

  <section class="intro">
    <div class="photo-stage" role="img" aria-label="Photo of the speaker in a dark suit holding a microphone at a conference"></div>
    <svg width="933" height="348" viewBox="0 0 933 348">
      <polygon points="520,0 933,0 933,348 522,348 376,176" fill="var(--gold)"/>
      <polygon points="536,0 933,0 933,348 538,348 392,176" fill="var(--blue)"/>
    </svg>
    <p class="bio">Daniel Mercer Stone is an internationally acclaimed marketing and sales strategist, author of eight books (including three international bestsellers), advisor to emerging companies, and professional speaker on topics including marketing, sales, and social media.</p>
  </section>

  <section class="praise">
    <span class="quote-open">&ldquo;</span>
    <p class="praise-text">Entertaining Motivational Credible Dynamic Bold Passionate Humorous Fresh Practical Captivating Engaging Actionable Enthusiastic Accessible <span class="quote-mark">&rdquo;</span></p>
  </section>

  <p class="highlight">He is the #1 international bestselling author of The Direct Playbook of Marketing and PR, now in its fourth edition with more than 300,000 copies sold in more than 25 languages from Bulgarian to Vietnamese.</p>

  <h2 class="topics-title">SPEAKING TOPICS</h2>
  <ul class="topics">
    <li class="topic">
      <h3>DIRECT PLAYBOOK OF MARKETING &amp; PR:</h3>
      <p>How to use social media, blogs, news releases, online video, and viral marketing to reach buyers directly</p>
    </li>
    <li class="topic">
      <h3>GROW YOUR BUSINESS NOW:</h3>
      <p>How to instantly engage your market and connect with customers in real time</p>
    </li>
    <li class="topic">
      <h3>AGILE SELLING IN A REAL-TIME WORLD:</h3>
      <p>How to succeed in a world where buyers are now in charge</p>
    </li>
  </ul>

  <div class="portrait" role="img" aria-label="Portrait of the speaker wearing a white headdress"></div>

  <div class="footer-rule"></div>
  <footer class="footer"></footer>
</div>
</body>
</html>
```